Pomme Sauvage Riding School Flyer Design

We need a flyer for our Horse riding school, called Pomme Sauvage Riding School.

At Pomme Sauvage Riding School, Horses and ponies are carefully matched to suit each rider's experience, ability and confidence. I am a Qualified instructor, equipped to train all levels from nervous beginners to the more advanced.

Horse riding is fun! Riders, particularly children, are taught not only skills on the horse, but skills that are integral to good horsemanship and ownership of horses.

We regularly host Ladies Days, Guest Instructors, 1 hour Trail Rides and Pony Ride Days!

We teach people how to interact safely with, and care for horses so they develop a genuine love and respect for the animals and the sport.

In addition to fundamental riding techniques including walk, trot, and canter, we teach our students:
Grooming and Care of horses, Safety around horses, Balance and Co-Ordination, How to saddle up and care for Tack, Responsibility for equipment and horse, Confidence and Confidence Building for all Ages.

Private and group lessons start at 5 years of age upwards.

We recommend children 4 years and under partake in 15 minute pony rides, mainly due to their attention span!

```html
<!DOCTYPE html>
<html lang="en">
<head>
<meta charset="utf-8">
<title>Pomme Sauvage Riding School</title>
<link href="https://fonts.googleapis.com/css2?family=Macondo&family=Roboto:wght@400&family=Arimo:wght@400&display=swap" rel="stylesheet">
<style>
  :root {
    --bg: #050505;
    --ink: #ffffff;
    --gold: #eea236;
    --gold-shadow: #3a1d00;
    --smoke: #5a5360;
    --rim-light: #e6e6e6;
    --rim-dark: #6b6b6b;
    --badge-core: #161616;
  }
  html, body { margin: 0; padding: 0; overflow: hidden; background: var(--bg); }
  .flyer {
    position: relative;
    width: 1200px;
    height: 850px;
    overflow: hidden;
    background:
      radial-gradient(ellipse 700px 260px at 780px 820px, rgba(120,110,125,.55), transparent 70%),
      radial-gradient(ellipse 600px 220px at 250px 860px, rgba(90,85,95,.45), transparent 70%),
      radial-gradient(ellipse 500px 300px at 60px 330px, rgba(80,78,88,.5), transparent 70%),
      var(--bg);
    font-family: "Arimo", Arial, sans-serif;
    color: var(--ink);
  }
  .fence-texture {
    position: absolute;
    left: 840px; top: 190px;
    width: 360px; height: 520px;
    background: radial-gradient(ellipse at 60% 40%, rgba(140,140,150,.35), transparent 70%);
  }
  .photo {
    position: absolute;
    border-radius: 50%;
    border: 5px solid #cfcfcf;
    box-shadow: 0 0 0 2px #555, 0 6px 18px rgba(0,0,0,.8);
  }
  .photo-grey-horse {
    left: -35px; top: -52px; width: 330px; height: 330px;
    background: radial-gradient(circle at 55% 45%, #4a4a4a, #9a9a9a 55%, #3a3a3a);
  }
  .photo-chestnut-horse {
    left: 878px; top: -45px; width: 335px; height: 310px;
    background: radial-gradient(circle at 45% 55%, #b3622a, #8a4a20 50%, #a69366 90%);
  }
  .brand {
    position: absolute;
    left: 300px; width: 600px; top: 212px;
    text-align: center;
    font-family: "Roboto", Arial, sans-serif;
    font-weight: 400;
    color: var(--ink);
  }
  .brand-name { font-size: 38px; letter-spacing: 7px; line-height: 46px; }
  .brand-sub { font-size: 20px; letter-spacing: 4px; margin-top: 10px; }
  .headline {
    position: absolute;
    left: 34px; top: 312px; width: 1150px;
    margin: 0;
    font-family: "Macondo", "Papyrus", fantasy;
    font-weight: 400;
    font-size: 27px;
    line-height: 37px;
    color: var(--gold);
    text-shadow: 2px 2px 3px var(--gold-shadow), 0 0 2px #000;
  }
  .body-copy {
    position: absolute;
    left: 32px; top: 447px; width: 590px;
    font-size: 14.5px;
    line-height: 24px;
    text-shadow: 1px 1px 2px #000;
  }
  .body-copy p { margin: 0 0 24px; }
  .body-copy p.tight { margin: 0; }
  .age-note {
    position: absolute;
    left: 695px; top: 515px; width: 490px;
    font-size: 21px; line-height: 26px;
  }
  .age-note .lead { font-size: 28px; line-height: 32px; display: block; }
  .badge { position: absolute; left: 822px; top: 622px; }
</style>
</head>
<body>
<main class="flyer">
  <div class="fence-texture" role="img" aria-label="Chain-link fence texture"></div>
  <div class="photo photo-grey-horse" role="img" aria-label="Photo of a grey horse standing by a white fence"></div>
  <div class="photo photo-chestnut-horse" role="img" aria-label="Photo of a chestnut horse with a white blaze"></div>

  <header class="brand">
    <div class="brand-name">POMME SAUVAGE</div>
    <div class="brand-sub">RIDING SCHOOL</div>
  </header>

  <h1 class="headline">At Pomme Sauvage Riding School, Horses and ponies are carefully matched to suit each rider's experience, ability and confidence. I am a Qualified instructor, equipped to train all levels from nervous beginners to the more advanced.</h1>

  <section class="body-copy">
    <p>Horse riding is fun! Riders, particularly children, are taught not only skills on the horse, but skills that are integral to good horsemanship and ownership of horses.</p>
    <p>We regularly host Ladies Days, Guest Instructors, 1 hour Trail Rides and Pony Ride Days!</p>
    <p>We teach people how to interact safely with, and care for horses so they develop a genuine love and respect for the animals and the sport.</p>
    <p class="tight">In addition to fundamental riding techniques including walk, trot, and canter, we teach our students:<br>Grooming and Care of horses, Safety around horses, Balance and Co-Ordination, How to saddle up and care for Tack, Responsibility for equipment and horse, Confidence and Confidence Building for all Ages.</p>
  </section>

  <p class="age-note"><span class="lead">We recommend children 4 years</span>and under partake in 15 minute pony rides, mainly due to their attention span!</p>

  <svg class="badge" width="220" height="220" viewBox="0 0 220 220" aria-label="Private and group lessons start at 5 years of age upwards">
    <defs>
      <linearGradient id="rim" x1="0" y1="0" x2="1" y2="1">
        <stop offset="0" stop-color="var(--rim-light)"/>
        <stop offset=".5" stop-color="var(--rim-dark)"/>
        <stop offset="1" stop-color="var(--rim-light)"/>
      </linearGradient>
      <path id="arc-top" d="M 30 110 A 80 80 0 0 1 190 110"/>
      <path id="arc-bottom" d="M 32 118 A 78 78 0 0 0 188 118"/>
    </defs>
    <circle cx="110" cy="110" r="104" fill="url(#rim)"/>
    <circle cx="110" cy="110" r="98" fill="#2a2a2a"/>
    <circle cx="110" cy="110" r="66" fill="url(#rim)"/>
    <circle cx="110" cy="110" r="61" fill="var(--badge-core)"/>
    <text font-family="Arimo, Arial, sans-serif" font-size="15" fill="#fff">
      <textPath href="#arc-top" startOffset="50%" text-anchor="middle">Private and group lessons start</textPath>
    </text>
    <text font-family="Arimo, Arial, sans-serif" font-size="20" fill="#fff" letter-spacing="1">
      <textPath href="#arc-bottom" startOffset="50%" text-anchor="middle" dominant-baseline="hanging">Upwards</textPath>
    </text>
    <g font-family="Arimo, Arial, sans-serif" font-size="21" fill="#fff" text-anchor="middle">
      <text x="110" y="90">AT</text>
      <text x="110" y="117">5 YEARS</text>
      <text x="110" y="143">OF AGE</text>
    </g>
  </svg>
</main>
</body>
</html>
```